LatAm Power Generation PPT - Corporate office in Houston, TX - USA

Here's our website: norvalepower.example. We are Norvale Power Management LLC. We are a small corporate office that manages power generation assets located in Latin America. We are pro clean energy, including thermal generation as long as it is gas-fired equipment (no coal-fired plants in our portfolio). Brazil is the first country where we have a presence in and we intend to grow significantly in the region in the next few years. We report to a private equity in the US, that is a co-investor. We would like a formal, elegant and detailed presentation for Board meetings, Budget reviews, Investment proposals, etc.
We have a logo/business cards just created with a CraftHive designer, which are uploaded.
Updates

Everyone: Focus of our core business is conventional energy, primarily thermal energy (except Coal). All the same, renewable energy is relevant, just not the sole objective. Thanks for participating!

```html
<!DOCTYPE html>
<html lang="en">
<head>
<meta charset="utf-8">
<title>Norvale Power – Presentation Templates</title>
<link href="https://fonts.googleapis.com/css2?family=Open+Sans:wght@400;600;700&display=swap" rel="stylesheet">
<style>
  :root{
    --navy:#0d0a6e;
    --navy-deep:#1c1f4f;
    --ink:#1e1a3a;
    --bar:#231f3a;
    --green:#1db04a;
    --green-deep:#0a7a30;
    --cream:#fdfdf4;
    --slate:#7a7880;
    --stone:#7a7872;
    --placeholder:#e4e4e4;
    --placeholder-text:#9a9a9a;
    --rule:#8d8d8d;
    --crimson:#c0184a;
    --white:#ffffff;
  }
  html,body{margin:0;padding:0;}
  body{
    width:1097px;height:1200px;overflow:hidden;position:relative;
    background:var(--white);
    font-family:"Open Sans",Arial,sans-serif;
  }
  .slide{position:absolute;display:block;}
  .slide--cover{left:0;top:3px;width:474px;height:366px;}
  .slide--hex-list{left:622px;top:0;width:475px;height:369px;}
  .slide--triptych{left:4px;top:421px;width:473px;height:366px;}
  .slide--callouts{left:622px;top:421px;width:475px;height:366px;}
  .slide--target{left:3px;top:833px;width:473px;height:367px;}
  .slide--pyramid{left:622px;top:831px;width:475px;height:369px;}
  svg text{font-family:"Open Sans",Arial,sans-serif;}
  .cover-title{font-size:56px;font-weight:700;fill:#000;}
  .cover-sub{font-size:25px;fill:#333;}
  .brand-name{font-size:25px;font-weight:600;fill:var(--green);}
  .headline{font-size:36px;font-weight:700;fill:var(--white);}
  .subhead{font-size:27px;font-weight:700;fill:var(--white);}
  .row-label{font-size:26px;fill:var(--ink);}
  .row-copy{font-size:17px;fill:var(--ink);}
  .photo-tag{font-size:12px;fill:var(--placeholder-text);text-anchor:middle;}
  .photo-tag--large{font-size:27px;}
  .panel-title{font-size:23px;font-weight:600;fill:var(--white);text-anchor:middle;}
  .panel-copy{font-size:20px;fill:var(--white);text-anchor:middle;}
  .callout-copy{font-size:16.5px;fill:var(--ink);text-anchor:middle;}
  .caption{font-size:23px;fill:var(--ink);text-anchor:middle;}
  .target-head{font-size:20px;font-weight:700;fill:var(--ink);}
  .target-copy{font-size:13px;fill:var(--ink);}
  .tier-label{font-size:18px;fill:var(--ink);text-anchor:middle;}
  .body-copy{font-size:17px;fill:var(--ink);}
</style>
</head>
<body>

<svg width="0" height="0" style="position:absolute" aria-hidden="true">
  <defs>
    <linearGradient id="greenFade" x1="0" y1="0" x2="1" y2="0">
      <stop offset="0" stop-color="#0a7a30"/>
      <stop offset="1" stop-color="#1db04a"/>
    </linearGradient>
    <linearGradient id="navyFade" x1="0" y1="0" x2="1" y2="0">
      <stop offset="0" stop-color="#1c1f4f"/>
      <stop offset="1" stop-color="#0d0a6e"/>
    </linearGradient>
    <linearGradient id="ribbonGreen" x1="0" y1="0" x2="0" y2="1">
      <stop offset="0" stop-color="#0a7a30"/>
      <stop offset="1" stop-color="#1db04a"/>
    </linearGradient>
    <linearGradient id="ringLine" x1="0" y1="0" x2="1" y2="1">
      <stop offset="0" stop-color="#c0184a"/>
      <stop offset="1" stop-color="#1c1f4f"/>
    </linearGradient>

    <g id="waveHeader">
      <rect x="0" y="0" width="797" height="140" fill="var(--cream)"/>
      <path d="M0 0 H797 V45 C700 35 600 30 480 45 C330 70 180 85 0 80 Z" fill="url(#navyFade)"/>
      <path d="M0 80 C180 85 330 70 480 45 C600 30 700 35 797 45 V68 C700 45 600 42 480 58 C330 80 180 118 0 135 Z" fill="url(#greenFade)"/>
      <rect x="0" y="86" width="482" height="50" fill="var(--bar)"/>
    </g>

    <g id="slantHeader">
      <rect x="0" y="0" width="797" height="116" fill="url(#navyFade)"/>
      <polygon points="0,0 797,0 797,116" fill="url(#greenFade)"/>
    </g>

    <polygon id="hexLarge" points="0,-62 54,-31 54,31 0,62 -54,31 -54,-31"/>
    <polygon id="hexSmall" points="0,-48 42,-24 42,24 0,48 -42,24 -42,-24"/>

    <g id="person">
      <circle cx="0" cy="0" r="14"/>
      <path d="M-22 48 V32 C-22 20 -12 17 0 17 C12 17 22 20 22 32 V48 Z"/>
    </g>
  </defs>
</svg>

<!-- Cover -->
<svg class="slide slide--cover" viewBox="0 0 796 615" preserveAspectRatio="none">
  <rect width="796" height="615" fill="var(--stone)"/>
  <rect x="40" y="185" width="756" height="239" fill="var(--white)"/>
  <path d="M0 0 H40 C30 150 40 400 62 615 H0 Z" fill="url(#navyFade)"/>
  <path d="M40 0 H48 C40 180 60 420 102 615 H62 C40 400 30 150 40 0 Z" fill="url(#ribbonGreen)"/>
  <circle cx="118" cy="303" r="22" fill="var(--green)"/>
  <text class="brand-name" x="150" y="312">Norvale Power</text>
  <text class="cover-title" x="333" y="267">PRESENTATION</text>
  <text class="cover-title" x="333" y="333">TEMPLATES</text>
  <text class="cover-sub" x="333" y="375">Aenean commodo ligula eget dolor</text>
</svg>

<!-- Hexagon list -->
<svg class="slide slide--hex-list" viewBox="0 0 797 620" preserveAspectRatio="none">
  <rect width="797" height="620" fill="var(--cream)"/>
  <use href="#waveHeader"/>
  <text class="headline" x="117" y="50">HEADLINE TEXT</text>
  <text class="subhead" x="345" y="121" text-anchor="middle">LOREM IPSUM</text>

  <g class="hex-row">
    <text class="row-label" x="270" y="241" text-anchor="end">ANEAN MASSA</text>
    <circle cx="304" cy="234" r="10" fill="var(--navy-deep)"/>
    <use href="#hexLarge" x="381" y="233" fill="var(--placeholder)" stroke="var(--green-deep)" stroke-width="6" role="img" aria-label="Photo placeholder"/>
    <text class="photo-tag" x="381" y="226">YOUR</text><text class="photo-tag" x="381" y="240">PHOTO</text><text class="photo-tag" x="381" y="254">HERE</text>
    <circle cx="456" cy="234" r="10" fill="var(--navy-deep)"/>
    <text class="row-copy" x="491" y="218">Quisque rutrum. Aenean</text>
    <text class="row-copy" x="491" y="238">imperdiet. Etiam ultricies nisi</text>
    <text class="row-copy" x="491" y="258">vel augue.</text>
  </g>
  <g class="hex-row">
    <text class="row-label" x="267" y="385" text-anchor="end">ANEAN MASSA</text>
    <circle cx="304" cy="378" r="10" fill="var(--navy-deep)"/>
    <use href="#hexLarge" x="381" y="378" fill="var(--placeholder)" stroke="var(--navy-deep)" stroke-width="6" role="img" aria-label="Photo placeholder"/>
    <text class="photo-tag" x="381" y="369">YOUR</text><text class="photo-tag" x="381" y="383">PHOTO</text><text class="photo-tag" x="381" y="397">HERE</text>
    <circle cx="456" cy="378" r="10" fill="var(--navy-deep)"/>
    <text class="row-copy" x="491" y="364">Quisque rutrum. Aenean</text>
    <text class="row-copy" x="491" y="384">imperdiet. Etiam ultricies nisi</text>
    <text class="row-copy" x="491" y="404">vel augue.</text>
  </g>
  <g class="hex-row">
    <text class="row-label" x="270" y="530" text-anchor="end">ANEAN MASSA</text>
    <circle cx="304" cy="522" r="10" fill="var(--navy-deep)"/>
    <use href="#hexLarge" x="381" y="522" fill="var(--placeholder)" stroke="var(--green)" stroke-width="6" role="img" aria-label="Photo placeholder"/>
    <text class="photo-tag" x="381" y="513">YOUR</text><text class="photo-tag" x="381" y="527">PHOTO</text><text class="photo-tag" x="381" y="541">HERE</text>
    <circle cx="456" cy="522" r="10" fill="var(--navy-deep)"/>
    <text class="row-copy" x="491" y="504">Quisque rutrum. Aenean</text>
    <text class="row-copy" x="491" y="524">imperdiet. Etiam ultricies nisi</text>
    <text class="row-copy" x="491" y="544">vel augue.</text>
  </g>
</svg>

<!-- Triptych -->
<svg class="slide slide--triptych" viewBox="0 0 795 615" preserveAspectRatio="none">
  <use href="#slantHeader"/>
  <text class="headline" x="36" y="78" style="font-size:34px">HEADLINE TEXT</text>
  <rect x="0" y="116" width="250" height="499" fill="var(--slate)"/>
  <rect x="541" y="116" width="254" height="499" fill="var(--slate)"/>
  <rect x="250" y="116" width="291" height="499" fill="var(--placeholder)" role="img" aria-label="Three photo placeholders split by a chevron"/>
  <polyline points="252,118 537,366 252,612" fill="none" stroke="var(--green-deep)" stroke-width="3"/>
  <text class="photo-tag photo-tag--large" x="462" y="170">YOUR</text>
  <text class="photo-tag photo-tag--large" x="462" y="201">PHOTO</text>
  <text class="photo-tag photo-tag--large" x="462" y="232">HERE</text>
  <text class="photo-tag photo-tag--large" x="345" y="334">YOUR</text>
  <text class="photo-tag photo-tag--large" x="345" y="365">PHOTO</text>
  <text class="photo-tag photo-tag--large" x="345" y="396">HERE</text>
  <text class="photo-tag photo-tag--large" x="462" y="513">YOUR</text>
  <text class="photo-tag photo-tag--large" x="462" y="544">PHOTO</text>
  <text class="photo-tag photo-tag--large" x="462" y="575">HERE</text>

  <text class="panel-title" x="123" y="204">Aenean commodo</text>
  <text class="panel-title" x="125" y="231">ligula eget dolor</text>
  <text class="panel-copy"><tspan x="125" y="288">Donec quam felis,</tspan><tspan x="125" dy="23.3">ultricies nec,</tspan><tspan x="125" dy="23.3">pellentesque eu,</tspan><tspan x="125" dy="23.3">pretium quis, sem.</tspan><tspan x="125" dy="23.3">Nulla consequat</tspan><tspan x="125" dy="23.3">massa quis enim.</tspan><tspan x="125" dy="23.3">Donec pede justo,</tspan><tspan x="125" dy="23.3">fringilla vel, aliquet</tspan><tspan x="125" dy="23.3">nec, vulputate eget,</tspan><tspan x="125" dy="23.3">arcu.</tspan></text>

  <text class="panel-title" x="675" y="196">Aenean commodo</text>
  <text class="panel-title" x="677" y="223">ligula eget dolor</text>
  <text class="panel-copy"><tspan x="677" y="281">Donec quam felis,</tspan><tspan x="677" dy="23.3">ultricies nec,</tspan><tspan x="677" dy="23.3">pellentesque eu,</tspan><tspan x="677" dy="23.3">pretium quis, sem.</tspan><tspan x="677" dy="23.3">Nulla consequat</tspan><tspan x="677" dy="23.3">massa quis enim.</tspan><tspan x="677" dy="23.3">Donec pede justo,</tspan><tspan x="677" dy="23.3">fringilla vel, aliquet</tspan><tspan x="677" dy="23.3">nec, vulputate eget,</tspan><tspan x="677" dy="23.3">arcu.</tspan></text>
</svg>

<!-- Callouts -->
<svg class="slide slide--callouts" viewBox="0 0 797 615" preserveAspectRatio="none">
  <rect width="797" height="615" fill="var(--cream)"/>
  <use href="#waveHeader"/>
  <text class="headline" x="117" y="50">HEADLINE TEXT</text>
  <text class="subhead" x="345" y="121" text-anchor="middle">LOREM IPSUM</text>

  <g fill="none" stroke="var(--navy-deep)" stroke-width="5" stroke-linejoin="miter">
    <path d="M50 175 H222 V403 H162 L136 455 L110 403 H50 Z"/>
    <path d="M308 175 H480 V403 H420 L394 455 L368 403 H308 Z"/>
    <path d="M564 175 H736 V403 H676 L650 455 L624 403 H564 Z"/>
  </g>
  <text class="callout-copy"><tspan x="136" y="229">Donec quam felis,</tspan><tspan x="136" dy="20">ultricies nec,</tspan><tspan x="136" dy="20">pellentesque eu,</tspan><tspan x="136" dy="20">pretium quis, sem.</tspan><tspan x="136" dy="20">Donec pede justo,</tspan><tspan x="136" dy="20">fringilla vel, aliquet</tspan><tspan x="136" dy="20">nec, vulputate</tspan><tspan x="136" dy="20">eget, arcu.</tspan></text>
  <text class="callout-copy"><tspan x="394" y="218">Donec quam felis,</tspan><tspan x="394" dy="20">ultricies nec,</tspan><tspan x="394" dy="20">pellentesque eu,</tspan><tspan x="394" dy="20">pretium quis, sem.</tspan><tspan x="394" dy="20">Donec pede justo,</tspan><tspan x="394" dy="20">fringilla vel, aliquet</tspan><tspan x="394" dy="20">nec, vulputate</tspan><tspan x="394" dy="20">eget, arcu.</tspan></text>
  <text class="callout-copy"><tspan x="650" y="222">Donec quam felis,</tspan><tspan x="650" dy="20">ultricies nec,</tspan><tspan x="650" dy="20">pellentesque eu,</tspan><tspan x="650" dy="20">pretium quis, sem.</tspan><tspan x="650" dy="20">Donec pede justo,</tspan><tspan x="650" dy="20">fringilla vel, aliquet</tspan><tspan x="650" dy="20">nec, vulputate</tspan><tspan x="650" dy="20">eget, arcu.</tspan></text>

  <g fill="var(--bar)" stroke="var(--cream)" stroke-width="3">
    <use href="#person" x="136" y="484"/>
    <use href="#person" transform="translate(372 472) scale(0.85)"/>
    <use href="#person" transform="translate(416 472) scale(0.85)"/>
    <use href="#person" transform="translate(394 490) scale(0.95)"/>
    <use href="#person" transform="translate(650 468) scale(0.7)"/>
    <use href="#person" transform="translate(630 490) scale(0.75)"/>
    <use href="#person" transform="translate(670 490) scale(0.75)"/>
    <use href="#person" transform="translate(650 506) scale(0.8)"/>
  </g>
  <text class="caption" x="138" y="570">ANEAN MASSA</text>
  <text class="caption" x="396" y="570">ANEAN MASSA</text>
  <text class="caption" x="652" y="570">ANEAN MASSA</text>
</svg>

<!-- Target diagram -->
<svg class="slide slide--target" viewBox="0 0 795 616" preserveAspectRatio="none">
  <rect width="795" height="616" fill="var(--cream)"/>
  <use href="#slantHeader"/>
  <text class="headline" x="23" y="86" style="font-size:34px">HEADLINE TEXT</text>

  <g fill="none" stroke-width="45" transform="translate(217 385)">
    <circle r="157" stroke="url(#navyFade)" stroke-dasharray="151 836" transform="rotate(235)"/>
    <circle r="157" stroke="url(#greenFade)" stroke-dasharray="77 910" transform="rotate(292)"/>
    <circle r="157" stroke="url(#greenFade)" stroke-dasharray="123 864" transform="rotate(345)"/>
    <circle r="157" stroke="url(#navyFade)" stroke-dasharray="274 713" transform="rotate(30)"/>
    <circle r="157" stroke="url(#ribbonGreen)" stroke-dasharray="288 699" transform="rotate(130)"/>
  </g>
  <g fill="none" stroke="url(#ringLine)" stroke-width="2">
    <circle cx="217" cy="385" r="90"/>
    <circle cx="217" cy="385" r="45"/>
    <circle cx="217" cy="385" r="10"/>
  </g>

  <g fill="none" stroke="var(--rule)" stroke-width="3">
    <polyline points="163,205 163,179 720,179"/>
    <polyline points="217,385 372,300 717,300"/>
    <line x1="392" y1="423" x2="720" y2="423"/>
  </g>

  <text class="target-head" x="465" y="168">LOREM IPSUM</text>
  <text class="target-copy" x="465" y="199">Li Europan lingues es membres del sam</text>
  <text class="target-copy" x="465" y="214">familie. Lor separat existentie es un myth.</text>
  <text class="target-head" x="430" y="292">LOREM IPSUM</text>
  <text class="target-copy" x="432" y="319">Li Europan lingues es membres del sam</text>
  <text class="target-copy" x="432" y="334">familie. Lor separat existentie es un myth.</text>
  <text class="target-head" x="432" y="414">LOREM IPSUM</text>
  <text class="target-copy" x="432" y="447">Li Europan lingues es membres del sam</text>
  <text class="target-copy" x="432" y="462">familie. Lor separat existentie es un myth.</text>
</svg>

<!-- Pyramid -->
<svg class="slide slide--pyramid" viewBox="0 0 797 620" preserveAspectRatio="none">
  <rect width="797" height="620" fill="var(--cream)"/>
  <use href="#waveHeader"/>
  <text class="headline" x="117" y="50">HEADLINE TEXT</text>
  <text class="subhead" x="345" y="121" text-anchor="middle">LOREM IPSUM</text>

  <g fill="var(--placeholder)" stroke="var(--green)" stroke-width="3">
    <use href="#hexSmall" x="85" y="246" role="img" aria-label="Photo placeholder"/>
    <use href="#hexSmall" x="169" y="246" role="img" aria-label="Photo placeholder"/>
    <use href="#hexSmall" x="127" y="325" role="img" aria-label="Photo placeholder"/>
    <use href="#hexSmall" x="697" y="219" role="img" aria-label="Photo placeholder"/>
    <use href="#hexSmall" x="673" y="388" role="img" aria-label="Photo placeholder"/>
  </g>
  <g class="photo-tag" style="font-size:10px">
    <text x="85" y="236">YOUR</text><text x="85" y="247">PHOTO</text><text x="85" y="258">HERE</text>
    <text x="169" y="236">YOUR</text><text x="169" y="247">PHOTO</text><text x="169" y="258">HERE</text>
    <text x="127" y="315">YOUR</text><text x="127" y="326">PHOTO</text><text x="127" y="337">HERE</text>
    <text x="697" y="209">YOUR</text><text x="697" y="220">PHOTO</text><text x="697" y="231">HERE</text>
    <text x="673" y="378">YOUR</text><text x="673" y="389">PHOTO</text><text x="673" y="400">HERE</text>
  </g>

  <g stroke="var(--rule)" stroke-width="3">
    <line x1="212" y1="302" x2="325" y2="302"/>
    <line x1="443" y1="224" x2="646" y2="224"/>
    <line x1="529" y1="388" x2="620" y2="388"/>
  </g>

  <g fill="none" stroke="var(--green-deep)" stroke-width="5">
    <polygon points="402,197 560,465 246,465"/>
    <line x1="360" y1="268" x2="444" y2="268"/>
    <line x1="315" y1="347" x2="490" y2="347"/>
    <line x1="270" y1="425" x2="536" y2="425"/>
  </g>
  <text class="tier-label" x="402" y="322">LOREM IPSUM</text>
  <text class="tier-label" x="397" y="391">ANEAN MASSA</text>
  <text class="tier-label" x="397" y="451">LOREM IPSUM</text>

  <text class="body-copy"><tspan x="91" y="528">Donec quam felis, ultricies nec, pellentesque eu, pretium quis, sem. Nulla</tspan><tspan x="91" dy="20">consequat massa quis enim. Donec pede justo, fringilla vel, aliquet nec,</tspan><tspan x="91" dy="20">vulputate eget, arcu.</tspan></text>
</svg>

</body>
</html>
```